Business Card for Flight Instructor/Commercial Pilot

I need a business card for myself as a Flight Instructor. I'm a certificated flight instructor at a local flight school in St Paul, MN and want to have a business card that I can give out both to prospective students and also to prospective employers in commercial/business aviation. The business card should have a few elements to it (my name, my position, and my ZRT certifications:
Dorian Welkes, MBA
Flight Instructor
CFI, CFII, AGI, IGI
Then lastly, I'd like it to include my phone number for calls or texts, my email address, and my Corvanet url. I'll provide all of these at a later point.

If we can include some kind of aviation graphic, that's great, but I don't currently have a logo and I don't necessarily need one, so don't feel like a logo is required here, it's not. I'm but I'm open to whatever you might put together. But I honestly don't need a logo, just good design with a simple graphic element to draw a little interest.
I'd also like to add a short tag line. A few ideas I have are:
- Fly Smart. Stay Humble. Never Stop Learning.
- Train smart. Fly safe. Have fun.
- Master the craft. Enjoy the flight.

For the back side, I'm open to ideas on what to put there. maybe the tagline could go there, or a QR code for my Corvanet page, or maybe something else.

Target audience is both prospective students who are interested in learning to fly (or adding more ratings) and commercial aviation companies that could be potential employer for me in commercial aviation. Trying to portray a sense of professionalism, trust, and high level of competency.

The business card doesn’t have to be standard (rectangular with square corners) and I’m open to suggestions for based on the design.
Lastly, I just don't want the design created by AI.
Let me know if you need any further info. Thanks!

```html
<!DOCTYPE html>
<html lang="en">
<head>
<meta charset="utf-8">
<title>Dorian Welkes — Flight Instructor</title>
<link rel="stylesheet" href="https://fonts.googleapis.com/css2?family=Inter:wght@400;800&display=swap">
<style>
  :root {
    --paper: #e8e7e0;
    --ink: #0c1018;
    --sky-night: #0f0f0f;
    --sky-deep: #0a1a3a;
    --sky-navy: #18287e;
    --sky-blue: #2740c8;
    --sky-azure: #2f62d0;
    --sky-teal: #32d6b8;
  }
  html, body {
    margin: 0;
    padding: 0;
    overflow: hidden;
    background: var(--paper);
  }
  .card {
    position: relative;
    width: 1200px;
    height: 686px;
    background: var(--paper);
    overflow: hidden;
    font-family: "Inter", Arial, sans-serif;
    color: var(--ink);
  }
  .sky-panel {
    position: absolute;
    inset: 0;
    width: 1200px;
    height: 686px;
  }
  .name {
    position: absolute;
    left: 33px;
    top: 0;
    margin: 0;
    font-weight: 800;
    font-size: 222px;
    line-height: 187px;
    letter-spacing: -0.055em;
    padding-top: 46px;
  }
  .name span { display: block; white-space: nowrap; }
  .credentials {
    position: absolute;
    left: 40px;
    top: 522px;
    margin: 0;
    font-weight: 400;
    font-size: 40px;
    line-height: 43px;
    letter-spacing: -0.05em;
  }
  .credentials span { display: block; }
</style>
</head>
<body>
  <main class="card">
    <svg class="sky-panel" viewBox="0 0 1200 686" aria-hidden="true">
      <defs>
        <linearGradient id="skyGradient" x1="0" y1="0" x2="0" y2="1">
          <stop offset="0" stop-color="var(--sky-night)"/>
          <stop offset="0.38" stop-color="var(--sky-deep)"/>
          <stop offset="0.56" stop-color="var(--sky-navy)"/>
          <stop offset="0.67" stop-color="var(--sky-blue)"/>
          <stop offset="0.8" stop-color="var(--sky-azure)"/>
          <stop offset="1" stop-color="var(--sky-teal)"/>
        </linearGradient>
      </defs>
      <path d="M914 0 H1200 V686 H696 C860 686 914 620 914 456 Z" fill="url(#skyGradient)"/>
    </svg>

    <h1 class="name"><span>Dorian</span><span>Welkes.</span></h1>

    <p class="credentials">
      <span>MBA</span>
      <span>Flight Instructor</span>
      <span>CFI, CFII, AGI, IGI</span>
    </p>
  </main>
</body>
</html>
```